PPT template for BLM. Whiskey, wine, food, drink and music. Moments in time

Velvet Crane and Cellars. Liquor, food, music. Need slides for BLM, Liquor, food and music.

Think whiskey distillery meets music studio.

Its about moments in time with the people we love. Music, food and drink all play apart in the times we remember.

Target Market(s)

Investors

Industry/Entity Type

Entertainment

Colors

Designer to choose colors to be used in the design.

Requirements
Must have
• Utilize the logo or image without text in all slides.
Nice to have
• blank template pages with logo or just image. multiple versions I can utilize. Logo and image as backgrounds, logo in corner and so on. Logo in many colors, rainbow, nautilus shell. Golden ratio....
Should not have
• Do not need close ups of food. its about people and experiences and food is part of this. Think tables, parties, events, chocolate fountains, and so on

```html
<!DOCTYPE html>
<html lang="en">
<head>
<meta charset="utf-8">
<title>BLM – Presentation Template Overview</title>
<link href="https://fonts.googleapis.com/css2?family=Cinzel:wght@400&family=Open+Sans:wght@300;400;600;700;800&display=swap" rel="stylesheet">
<style>
  :root{
    --canvas:#f1f1f1;
    --slide:#2a2a2a;
    --slide-deep:#222222;
    --green:#8cc63e;
    --lime:#a8e22c;
    --mid:#6fae2a;
    --deep:#3f7a1a;
    --white:#ffffff;
    --text:#e8e8e8;
    --muted:#8c8c8c;
    --map:#d6d6d6;
  }
  html,body{margin:0;padding:0;overflow:hidden}
  body{width:1200px;height:3363px;background:var(--canvas);position:relative;font-family:"Open Sans",Arial,sans-serif}
  .hero{position:absolute;left:23px;top:20px;width:1154px;height:649px;overflow:hidden}
  .slide{position:absolute;width:571px;height:321px;overflow:hidden;background:var(--slide)}
  .slide svg,.hero svg{display:block;width:100%;height:100%}
  .col-a{left:23px}.col-b{left:606px}
  .r1{top:682px}.r2{top:1015px}.r3{top:1348px}.r4{top:1681px}
  .r5{top:2014px}.r6{top:2347px}.r7{top:2680px}.r8{top:3013px}
  svg text{font-family:"Open Sans",Arial,sans-serif}
  .title{fill:var(--white);font-weight:700;font-size:15px}
  .title-wide{fill:var(--white);font-weight:700;font-size:12px;letter-spacing:1.6px}
  .head{fill:var(--green);font-weight:700;font-size:5.5px}
  .label{fill:var(--white);font-weight:600;font-size:5.5px}
  .body{fill:var(--muted);font-size:3.6px}
  .stat{fill:var(--white);font-weight:700;font-size:13px}
  .brand{font-family:"Cinzel",serif;fill:var(--white)}
  .hero-copy{fill:var(--white);font-size:10px;font-weight:300}
  .corner-mark{fill:var(--green);font-weight:700;font-size:6px;letter-spacing:0.8px}
</style>
</head>
<body>

<!-- Cover -->
<section class="hero">
  <svg viewBox="0 0 883 497" preserveAspectRatio="none">
    <defs>
      <radialGradient id="heroGlow" cx="0.33" cy="0.4" r="0.75">
        <stop offset="0" stop-color="#b8e83a"/>
        <stop offset="0.25" stop-color="#3f8e1c"/>
        <stop offset="0.6" stop-color="#0f3a10"/>
        <stop offset="1" stop-color="#041406"/>
      </radialGradient>
      <linearGradient id="bottleFill" x1="0" y1="0" x2="1" y2="0">
        <stop offset="0" stop-color="#1f8f1a"/>
        <stop offset="0.5" stop-color="#5fe23a"/>
        <stop offset="1" stop-color="#1c7a16"/>
      </linearGradient>
    </defs>
    <rect width="883" height="497" fill="url(#heroGlow)"/>
    <rect x="112" y="25" width="330" height="472" rx="30" fill="url(#bottleFill)" opacity="0.55" role="img" aria-label="Green liquor bottle with blank label beside a filled shot glass"/>
    <circle cx="660" cy="165" r="40" fill="none" stroke="var(--white)" stroke-width="3"/>
    <text class="brand" x="660" y="175" text-anchor="middle" font-size="26">BLM</text>
    <text class="brand" x="660" y="241" text-anchor="middle" font-size="28" letter-spacing="8">VELVET CRANE</text>
    <text class="brand" x="660" y="257" text-anchor="middle" font-size="8" letter-spacing="6">AND CELLARS</text>
    <text class="hero-copy" x="660" y="289" text-anchor="middle">On the other hand, we denounce with righteous indignation and</text>
    <text class="hero-copy" x="660" y="301" text-anchor="middle">dislike men who are so beguiled and demoralized by the charms</text>
    <text class="hero-copy" x="660" y="313" text-anchor="middle">of pleasure of the moment</text>
    <rect x="584" y="338" width="154" height="33" rx="5" fill="none" stroke="var(--white)" stroke-width="2"/>
    <text x="661" y="360" text-anchor="middle" fill="var(--white)" font-size="14" font-weight="300">Lorem ipsum</text>
  </svg>
</section>

<!-- Slide: mockup desktop -->
<section class="slide col-a r1">
  <svg viewBox="0 0 437 246" preserveAspectRatio="none">
    <g fill="var(--green)"><circle cx="6" cy="6" r="1.6"/><circle cx="11" cy="6" r="1.6"/><circle cx="16" cy="6" r="1.6"/></g>
    <text class="corner-mark" x="430" y="10" text-anchor="end">BLM</text>
    <circle cx="437" cy="246" r="12" fill="var(--green)"/>
    <text class="title" x="33" y="75">Beautiful Mockup</text>
    <rect x="37" y="82" width="20" height="2" fill="var(--green)"/><rect x="60" y="82" width="6" height="2" fill="var(--green)"/>
    <g>
      <circle cx="45" cy="105" r="9" fill="var(--green)"/><text class="head" x="62" y="102">consectetur adipiscing</text>
      <text class="body" x="62" y="108">Lorem ipsum dolor sit amet, sed do eiusmod</text><text class="body" x="62" y="113">tempor incididunt ut labore et dolore</text>
      <circle cx="45" cy="139" r="9" fill="var(--green)"/><text class="head" x="62" y="136">consectetur adipiscing</text>
      <text class="body" x="62" y="142">Lorem ipsum dolor sit amet, sed do eiusmod</text><text class="body" x="62" y="147">tempor incididunt ut labore et dolore</text>
      <circle cx="45" cy="173" r="9" fill="var(--green)"/><text class="head" x="62" y="170">consectetur adipiscing</text>
      <text class="body" x="62" y="176">Lorem ipsum dolor sit amet, sed do eiusmod</text><text class="body" x="62" y="181">tempor incididunt ut labore et dolore</text>
    </g>
    <circle cx="330" cy="75" r="62" fill="var(--lime)"/>
    <circle cx="400" cy="168" r="14" fill="var(--green)"/>
    <circle cx="250" cy="25" r="4" fill="var(--green)"/>
    <rect x="225" y="20" width="170" height="190" rx="6" fill="#5a5a5a" role="img" aria-label="Desktop computer mockup showing a plated steak dinner"/>
  </svg>
</section>

<!-- Slide: mockup multiple screens -->
<section class="slide col-b r1">
  <svg viewBox="0 0 437 246" preserveAspectRatio="none">
    <g fill="var(--green)"><circle cx="6" cy="6" r="1.6"/><circle cx="11" cy="6" r="1.6"/><circle cx="16" cy="6" r="1.6"/></g>
    <text class="corner-mark" x="430" y="10" text-anchor="end">BLM</text>
    <circle cx="437" cy="246" r="12" fill="var(--green)"/>
    <circle cx="150" cy="75" r="55" fill="var(--lime)"/>
    <circle cx="225" cy="78" r="12" fill="var(--green)"/>
    <rect x="25" y="55" width="245" height="130" rx="5" fill="#5a5a5a" role="img" aria-label="Row of computer screens showing fresh salads and sandwiches"/>
    <text class="title" x="278" y="77">Beautiful Mockup</text>
    <rect x="282" y="84" width="20" height="2" fill="var(--green)"/><rect x="305" y="84" width="6" height="2" fill="var(--green)"/>
    <text class="body" x="278" y="98">Lorem ipsum dolor sit amet, consectetur adipiscing elit</text>
    <text class="body" x="278" y="103">sed do eiusmod tempor incididunt ut labore et</text>
    <text class="body" x="278" y="108">dolore magna aliqua ut enim ad minim veniam</text>
    <text class="body" x="278" y="113">quis nostrud exercitation ullamco laboris nisi</text>
    <rect x="278" y="138" width="142" height="28" fill="none" stroke="var(--green)" stroke-width="1"/>
    <circle cx="292" cy="152" r="8" fill="var(--green)"/>
    <text class="label" x="306" y="149">suscipit lobortis nisl</text><text class="body" x="306" y="156">Nulla facilisi morbi tempus iaculis urna</text>
    <rect x="278" y="176" width="142" height="28" fill="none" stroke="var(--green)" stroke-width="1"/>
    <circle cx="292" cy="190" r="8" fill="var(--green)"/>
    <text class="label" x="306" y="187">suscipit lobortis nisl</text><text class="body" x="306" y="194">Nulla facilisi morbi tempus iaculis urna</text>
  </svg>
</section>

<!-- Slide: mockup laptop -->
<section class="slide col-a r2">
  <svg viewBox="0 0 437 246" preserveAspectRatio="none">
    <g fill="var(--green)"><circle cx="6" cy="6" r="1.6"/><circle cx="11" cy="6" r="1.6"/><circle cx="16" cy="6" r="1.6"/></g>
    <text class="corner-mark" x="430" y="10" text-anchor="end">BLM</text>
    <circle cx="437" cy="246" r="12" fill="var(--green)"/>
    <text class="title" x="22" y="72">Beautiful Mockup</text>
    <rect x="26" y="79" width="20" height="2" fill="var(--green)"/><rect x="49" y="79" width="6" height="2" fill="var(--green)"/>
    <text class="body" x="22" y="95">Lorem ipsum dolor sit amet, consectetur adipiscing elit sed</text>
    <text class="body" x="22" y="100">do eiusmod tempor incididunt ut labore et dolore</text>
    <text class="body" x="22" y="105">magna aliqua ut enim ad minim veniam quis</text>
    <text class="body" x="22" y="110">nostrud exercitation ullamco laboris nisi ut aliquip</text>
    <text class="body" x="22" y="115">ex ea commodo consequat duis aute irure</text>
    <g fill="none" stroke="var(--text)" stroke-width="1.2">
      <ellipse cx="38" cy="142" rx="7" ry="4"/><path d="M100 146h14M102 146a5 5 0 0 1 10 0"/><path d="M160 146h14l-3-8h-8z"/>
    </g>
    <text class="head" x="22" y="158">Lorem ipsum</text><text class="head" x="88" y="158">Lorem ipsum</text><text class="head" x="152" y="158">Lorem ipsum</text>
    <text class="body" x="22" y="165">Sed ut perspiciatis unde</text><text class="body" x="88" y="165">Sed ut perspiciatis unde</text><text class="body" x="152" y="165">Sed ut perspiciatis unde</text>
    <circle cx="400" cy="175" r="35" fill="var(--lime)"/>
    <circle cx="240" cy="45" r="16" fill="var(--green)"/>
    <circle cx="268" cy="26" r="4" fill="var(--green)"/>
    <rect x="245" y="55" width="192" height="122" rx="4" fill="#5a5a5a" role="img" aria-label="Laptop mockup showing a shared dinner table spread"/>
  </svg>
</section>

<!-- Slide: mockup phone -->
<section class="slide col-b r2">
  <svg viewBox="0 0 437 246" preserveAspectRatio="none">
    <g fill="var(--green)"><circle cx="6" cy="6" r="1.6"/><circle cx="11" cy="6" r="1.6"/><circle cx="16" cy="6" r="1.6"/></g>
    <text class="corner-mark" x="430" y="10" text-anchor="end">BLM</text>
    <circle cx="437" cy="246" r="12" fill="var(--green)"/>
    <circle cx="110" cy="110" r="65" fill="var(--lime)"/>
    <circle cx="48" cy="178" r="14" fill="var(--green)"/>
    <circle cx="72" cy="160" r="3" fill="var(--green)"/>
    <rect x="50" y="22" width="150" height="224" rx="8" fill="#5a5a5a" role="img" aria-label="Hand holding a smartphone that shows a burger"/>
    <text class="title" x="252" y="72">Beautiful Mockup</text>
    <rect x="256" y="79" width="20" height="2" fill="var(--green)"/><rect x="279" y="79" width="6" height="2" fill="var(--green)"/>
    <text class="body" x="252" y="95">Lorem ipsum dolor sit amet, consectetur adipiscing elit sed</text>
    <text class="body" x="252" y="100">do eiusmod tempor incididunt ut labore et dolore</text>
    <text class="body" x="252" y="105">magna aliqua ut enim ad minim veniam quis</text>
    <text class="body" x="252" y="110">nostrud exercitation ullamco laboris nisi ut aliquip</text>
    <text class="body" x="252" y="115">ex ea commodo consequat duis aute irure</text>
    <rect x="252" y="135" width="46" height="42" fill="var(--lime)"/>
    <text class="stat" x="275" y="156" text-anchor="middle">759K</text><text class="body" x="275" y="165" text-anchor="middle" fill="var(--white)">Lorem ipsum dolor</text>
    <rect x="303" y="135" width="46" height="42" fill="var(--lime)"/>
    <text class="stat" x="326" y="156" text-anchor="middle">98%</text><text class="body" x="326" y="165" text-anchor="middle" fill="var(--white)">Lorem ipsum dolor</text>
  </svg>
</section>

<!-- Slide: infographic venn -->
<section class="slide col-a r3">
  <svg viewBox="0 0 437 246" preserveAspectRatio="none">
    <g fill="var(--green)"><circle cx="6" cy="6" r="1.6"/><circle cx="11" cy="6" r="1.6"/><circle cx="16" cy="6" r="1.6"/></g>
    <text class="corner-mark" x="430" y="10" text-anchor="end">BLM</text>
    <circle cx="437" cy="246" r="12" fill="var(--green)"/>
    <text class="title-wide" x="218" y="28" text-anchor="middle">Infographic Slide</text>
    <rect x="200" y="34" width="20" height="2" fill="var(--green)"/><rect x="223" y="34" width="6" height="2" fill="var(--green)"/>
    <text class="body" x="218" y="44" text-anchor="middle">Lorem ipsum dolor sit amet, consectetur adipiscing elit, sed do eiusmod tempor incididunt ut labore</text>
    <text class="body" x="218" y="49" text-anchor="middle">et dolore magna aliqua ut enim ad minim veniam quis nostrud exercitation</text>
    <circle cx="220" cy="118" r="38" fill="var(--mid)" opacity="0.9"/>
    <circle cx="197" cy="160" r="38" fill="var(--green)" opacity="0.85"/>
    <circle cx="243" cy="160" r="38" fill="var(--lime)" opacity="0.8"/>
    <circle cx="220" cy="146" r="14" fill="var(--slide)"/>
    <text class="label" x="220" y="98" text-anchor="middle">Keyword</text>
    <text class="label" x="180" y="175" text-anchor="middle">Keyword</text>
    <text class="label" x="262" y="175" text-anchor="middle">Keyword</text>
    <text class="body" x="220" y="104" text-anchor="middle" fill="var(--white)">Sed ut perspiciatis</text>
    <text class="body" x="180" y="181" text-anchor="middle" fill="var(--white)">Sed ut perspiciatis</text>
    <text class="body" x="262" y="181" text-anchor="middle" fill="var(--white)">Sed ut perspiciatis</text>
    <text class="label" x="65" y="95">Lorem Ipsum</text><text class="label" x="325" y="95">Lorem Ipsum</text>
    <text class="label" x="65" y="185">Lorem Ipsum</text><text class="label" x="325" y="185">Lorem Ipsum</text>
    <g class="body">
      <text x="35" y="103">Sed ut perspiciatis unde omnis</text><text x="35" y="108">iste natus error sit voluptatem</text><text x="35" y="113">accusantium doloremque laudantium totam</text>
      <text x="325" y="103">Sed ut perspiciatis unde omnis</text><text x="325" y="108">iste natus error sit voluptatem</text><text x="325" y="113">accusantium doloremque laudantium totam</text>
      <text x="35" y="193">Sed ut perspiciatis unde omnis</text><text x="35" y="198">iste natus error sit voluptatem</text><text x="35" y="203">accusantium doloremque laudantium totam</text>
      <text x="325" y="193">Sed ut perspiciatis unde omnis</text><text x="325" y="198">iste natus error sit voluptatem</text><text x="325" y="203">accusantium doloremque laudantium totam</text>
    </g>
  </svg>
</section>

<!-- Slide: infographic circles -->
<section class="slide col-b r3">
  <svg viewBox="0 0 437 246" preserveAspectRatio="none">
    <g fill="var(--green)"><circle cx="6" cy="6" r="1.6"/><circle cx="11" cy="6" r="1.6"/><circle cx="16" cy="6" r="1.6"/></g>
    <text class="corner-mark" x="430" y="10" text-anchor="end">BLM</text>
    <circle cx="437" cy="246" r="12" fill="var(--green)"/>
    <text class="title-wide" x="218" y="28" text-anchor="middle">Infographic Slide</text>
    <rect x="200" y="34" width="20" height="2" fill="var(--green)"/><rect x="223" y="34" width="6" height="2" fill="var(--green)"/>
    <text class="body" x="218" y="44" text-anchor="middle">Lorem ipsum dolor sit amet, consectetur adipiscing elit, sed do eiusmod tempor incididunt ut labore</text>
    <text class="body" x="218" y="49" text-anchor="middle">et dolore magna aliqua ut enim ad minim veniam quis nostrud exercitation</text>
    <circle cx="205" cy="105" r="28" fill="var(--deep)"/>
    <circle cx="150" cy="140" r="30" fill="var(--green)"/>
    <circle cx="225" cy="168" r="30" fill="var(--lime)"/>
    <circle cx="285" cy="140" r="30" fill="var(--mid)"/>
    <g fill="none" stroke="var(--white)" stroke-width="1.2">
      <ellipse cx="150" cy="140" rx="10" ry="6"/><path d="M198 100v12M205 98v14M212 100v12"/>
      <path d="M215 172h20M218 172a7 7 0 0 1 14 0"/><path d="M275 146h20l-4-10h-12z"/>
    </g>
    <text class="head" x="150" y="77">Lorem ipsum</text><text class="body" x="125" y="84">Lorem ipsum is simply dummy text of</text>
    <text class="head" x="60" y="128">Lorem ipsum</text><text class="body" x="60" y="135">Lorem ipsum is simply dummy text</text>
    <text class="head" x="330" y="128">Lorem ipsum</text><text class="body" x="330" y="135">Lorem ipsum is simply dummy text</text>
    <text class="head" x="255" y="206">Lorem ipsum</text><text class="body" x="255" y="213">Lorem ipsum is simply dummy text</text>
  </svg>
</section>

<!-- Slide: infographic pyramid -->
<section class="slide col-a r4">
  <svg viewBox="0 0 437 246" preserveAspectRatio="none">
    <g fill="var(--green)"><circle cx="6" cy="6" r="1.6"/><circle cx="11" cy="6" r="1.6"/><circle cx="16" cy="6" r="1.6"/></g>
    <text class="corner-mark" x="430" y="10" text-anchor="end">BLM</text>
    <circle cx="437" cy="246" r="12" fill="var(--green)"/>
    <text class="title-wide" x="218" y="28" text-anchor="middle">Infographic Slide</text>
    <rect x="200" y="34" width="20" height="2" fill="var(--green)"/><rect x="223" y="34" width="6" height="2" fill="var(--green)"/>
    <text class="body" x="218" y="44" text-anchor="middle">Lorem ipsum dolor sit amet, consectetur adipiscing elit, sed do eiusmod tempor incididunt ut labore</text>
    <text class="body" x="218" y="49" text-anchor="middle">et dolore magna aliqua ut enim ad minim veniam quis nostrud exercitation</text>
    <g>
      <rect x="203" y="85" width="32" height="30" fill="var(--deep)"/>
      <rect x="186" y="115" width="32" height="30" fill="var(--mid)"/><rect x="220" y="115" width="32" height="30" fill="var(--green)"/>
      <rect x="169" y="145" width="32" height="30" fill="var(--green)"/><rect x="203" y="145" width="32" height="30" fill="var(--mid)"/><rect x="237" y="145" width="32" height="30" fill="var(--lime)"/>
      <rect x="152" y="175" width="32" height="30" fill="var(--lime)"/><rect x="186" y="175" width="32" height="30" fill="var(--green)"/><rect x="220" y="175" width="32" height="30" fill="var(--lime)"/><rect x="254" y="175" width="32" height="30" fill="var(--mid)"/>
      <g fill="var(--white)"><circle cx="219" cy="100" r="7"/><circle cx="202" cy="130" r="7"/><circle cx="236" cy="130" r="7"/><circle cx="185" cy="160" r="7"/><circle cx="219" cy="160" r="7"/><circle cx="253" cy="160" r="7"/></g>
    </g>
    <g>
      <text class="head" x="130" y="70">Lorem ipsum</text><text class="body" x="110" y="77">Lorem ipsum dolor sit</text><text class="body" x="110" y="82">consectetur elit sed do</text><text class="body" x="110" y="87">tempor incididunt ut labore</text>
      <text class="head" x="105" y="126">Lorem ipsum</text><text class="body" x="85" y="133">Lorem ipsum dolor sit</text><text class="body" x="85" y="138">consectetur elit sed do</text><text class="body" x="85" y="143">tempor incididunt ut labore</text>
      <text class="head" x="80" y="182">Lorem ipsum</text><text class="body" x="60" y="189">Lorem ipsum dolor sit</text><text class="body" x="60" y="194">consectetur elit sed do</text><text class="body" x="60" y="199">tempor incididunt ut labore</text>
      <text class="head" x="268" y="70">Lorem ipsum</text><text class="body" x="268" y="77">Lorem ipsum dolor sit</text><text class="body" x="268" y="82">consectetur elit sed do</text><text class="body" x="268" y="87">tempor incididunt ut labore</text>
      <text class="head" x="293" y="126">Lorem ipsum</text><text class="body" x="293" y="133">Lorem ipsum dolor sit</text><text class="body" x="293" y="138">consectetur elit sed do</text><text class="body" x="293" y="143">tempor incididunt ut labore</text>
      <text class="head" x="318" y="182">Lorem ipsum</text><text class="body" x="318" y="189">Lorem ipsum dolor sit</text><text class="body" x="318" y="194">consectetur elit sed do</text><text class="body" x="318" y="199">tempor incididunt ut labore</text>
    </g>
  </svg>
</section>

<!-- Slide: infographic wave -->
<section class="slide col-b r4">
  <svg viewBox="0 0 437 246" preserveAspectRatio="none">
    <g fill="var(--green)"><circle cx="6" cy="6" r="1.6"/><circle cx="11" cy="6" r="1.6"/><circle cx="16" cy="6" r="1.6"/></g>
    <text class="corner-mark" x="430" y="10" text-anchor="end">BLM</text>
    <circle cx="437" cy="246" r="12" fill="var(--green)"/>
    <text class="title-wide" x="218" y="28" text-anchor="middle">Infographic Slide</text>
    <rect x="200" y="34" width="20" height="2" fill="var(--green)"/><rect x="223" y="34" width="6" height="2" fill="var(--green)"/>
    <text class="body" x="218" y="44" text-anchor="middle">Lorem ipsum dolor sit amet, consectetur adipiscing elit, sed do eiusmod tempor incididunt ut labore</text>
    <text class="body" x="218" y="49" text-anchor="middle">et dolore magna aliqua ut enim ad minim veniam quis nostrud exercitation</text>
    <path d="M45 160 C45 120 90 100 90 100 C130 100 135 140 135 145 C135 185 175 190 175 190 C215 190 215 150 215 145 C215 105 255 100 255 100 C295 100 300 140 300 145 C300 185 345 190 345 190 C385 190 390 150 390 145" fill="none" stroke="var(--green)" stroke-width="6" stroke-linecap="round"/>
    <g fill="var(--white)" stroke="var(--green)" stroke-width="2"><circle cx="90" cy="100" r="4"/><circle cx="175" cy="190" r="4"/><circle cx="255" cy="100" r="4"/><circle cx="345" cy="190" r="4"/></g>
    <g fill="var(--mid)"><circle cx="90" cy="145" r="16"/><circle cx="175" cy="145" r="16"/><circle cx="255" cy="145" r="16"/><circle cx="345" cy="145" r="16"/></g>
    <text class="head" x="175" y="92" text-anchor="middle">Lorem ipsum</text><text class="body" x="175" y="99" text-anchor="middle">Lorem ipsum dolor sit</text><text class="body" x="175" y="104" text-anchor="middle">consectetur elit sed do</text><text class="body" x="175" y="109" text-anchor="middle">tempor incididunt ut labore</text>
    <text class="head" x="345" y="92" text-anchor="middle">Lorem ipsum</text><text class="body" x="345" y="99" text-anchor="middle">Lorem ipsum dolor sit</text><text class="body" x="345" y="104" text-anchor="middle">consectetur elit sed do</text><text class="body" x="345" y="109" text-anchor="middle">tempor incididunt ut labore</text>
    <text class="head" x="90" y="203" text-anchor="middle">Lorem ipsum</text><text class="body" x="90" y="210" text-anchor="middle">Lorem ipsum dolor sit</text><text class="body" x="90" y="215" text-anchor="middle">consectetur elit sed do</text><text class="body" x="90" y="220" text-anchor="middle">tempor incididunt ut labore</text>
    <text class="head" x="255" y="203" text-anchor="middle">Lorem ipsum</text><text class="body" x="255" y="210" text-anchor="middle">Lorem ipsum dolor sit</text><text class="body" x="255" y="215" text-anchor="middle">consectetur elit sed do</text><text class="body" x="255" y="220" text-anchor="middle">tempor incididunt ut labore</text>
  </svg>
</section>

<!-- Slide: radar chart -->
<section class="slide col-a r5">
  <svg viewBox="0 0 437 246" preserveAspectRatio="none">
    <g fill="var(--green)"><circle cx="6" cy="6" r="1.6"/><circle cx="11" cy="6" r="1.6"/><circle cx="16" cy="6" r="1.6"/></g>
    <text class="corner-mark" x="430" y="10" text-anchor="end">BLM</text>
    <circle cx="437" cy="246" r="12" fill="var(--green)"/>
    <text class="title" x="35" y="55">Infographic Slide</text>
    <rect x="39" y="62" width="20" height="2" fill="var(--green)"/><rect x="62" y="62" width="6" height="2" fill="var(--green)"/>
    <text class="body" x="35" y="76">Lorem ipsum dolor sit amet, consectetur adipiscing</text>
    <text class="body" x="35" y="81">elit sed do eiusmod tempor incididunt ut</text>
    <text class="body" x="35" y="86">labore et dolore magna aliqua ut enim</text>
    <g>
      <circle cx="45" cy="110" r="9" fill="var(--green)"/><text class="head" x="62" y="107">consectetur adipiscing</text><text class="body" x="62" y="113">Lorem ipsum dolor sit amet sed</text><text class="body" x="62" y="118">do eiusmod tempor incididunt labore</text>
      <circle cx="45" cy="143" r="9" fill="var(--green)"/><text class="head" x="62" y="140">consectetur adipiscing</text><text class="body" x="62" y="146">Lorem ipsum dolor sit amet sed</text><text class="body" x="62" y="151">do eiusmod tempor incididunt labore</text>
      <circle cx="45" cy="176" r="9" fill="var(--green)"/><text class="head" x="62" y="173">consectetur adipiscing</text><text class="body" x="62" y="179">Lorem ipsum dolor sit amet sed</text><text class="body" x="62" y="184">do eiusmod tempor incididunt labore</text>
    </g>
    <g fill="none" stroke="#bdbdbd" stroke-width="0.6">
      <circle cx="305" cy="120" r="72"/><circle cx="305" cy="120" r="48"/><circle cx="305" cy="120" r="24"/>
      <path d="M305 48V192M233 120H377M254 69L356 171M356 69L254 171"/>
    </g>
    <polygon points="305,62 335,90 355,120 345,160 305,182 280,145 262,120 278,92" fill="var(--mid)" opacity="0.95"/>
    <polygon points="305,85 325,100 330,120 318,140 305,150 290,135 285,120 292,105" fill="#555" opacity="0.7"/>
    <g class="body" fill="var(--text)">
      <text x="305" y="44" text-anchor="middle">Chicken</text><text x="358" y="66">Fish</text><text x="381" y="122">Veggie</text><text x="358" y="178">Beef</text>
      <text x="305" y="200" text-anchor="middle">Potato</text><text x="240" y="178">Hot Dog</text><text x="216" y="122">Burger</text><text x="240" y="66">Pizza</text>
    </g>
    <circle cx="280" cy="213" r="2" fill="var(--green)"/><text class="body" x="285" y="214.5" fill="var(--text)">Lorem</text>
    <circle cx="315" cy="213" r="2" fill="#666"/><text class="body" x="320" y="214.5" fill="var(--text)">Ipsum</text>
  </svg>
</section>

<!-- Slide: chart diagram with stats -->
<section class="slide col-b r5">
  <svg viewBox="0 0 437 246" preserveAspectRatio="none">
    <g fill="var(--green)"><circle cx="6" cy="6" r="1.6"/><circle cx="11" cy="6" r="1.6"/><circle cx="16" cy="6" r="1.6"/></g>
    <text class="corner-mark" x="430" y="10" text-anchor="end">BLM</text>
    <circle cx="437" cy="246" r="12" fill="var(--green)"/>
    <text class="title-wide" x="218" y="28" text-anchor="middle">Chart Diagram</text>
    <rect x="200" y="34" width="20" height="2" fill="var(--green)"/><rect x="223" y="34" width="6" height="2" fill="var(--green)"/>
    <text class="body" x="218" y="44" text-anchor="middle">Lorem ipsum dolor sit amet, consectetur adipiscing elit, sed do eiusmod tempor incididunt ut labore</text>
    <text class="body" x="218" y="49" text-anchor="middle">et dolore magna aliqua ut enim ad minim veniam quis nostrud exercitation</text>
    <g>
      <rect x="40" y="88" width="50" height="45" fill="var(--lime)"/><text class="stat" x="65" y="108" text-anchor="middle">59%</text><text class="body" x="65" y="118" text-anchor="middle" fill="var(--white)">Lorem ipsum dolor sit</text>
      <rect x="96" y="88" width="50" height="45" fill="var(--lime)"/><text class="stat" x="121" y="108" text-anchor="middle">69%</text><text class="body" x="121" y="118" text-anchor="middle" fill="var(--white)">Lorem ipsum dolor sit</text>
      <rect x="40" y="140" width="50" height="45" fill="var(--lime)"/><text class="stat" x="65" y="160" text-anchor="middle">78%</text><text class="body" x="65" y="170" text-anchor="middle" fill="var(--white)">Lorem ipsum dolor sit</text>
      <rect x="96" y="140" width="50" height="45" fill="var(--lime)"/><text class="stat" x="121" y="160" text-anchor="middle">98%</text><text class="body" x="121" y="170" text-anchor="middle" fill="var(--white)">Lorem ipsum dolor sit</text>
    </g>
    <text class="body" x="295" y="80" text-anchor="middle" fill="var(--text)">Chart Title</text>
    <g fill="none" stroke="#888" stroke-width="0.5"><path d="M195 100v85l60 25M195 185l180-20M255 210l135-25M195 100l180-5"/></g>
    <polygon points="205,120 245,110 280,135 320,115 385,112 365,140 330,138 290,145 255,150" fill="var(--mid)"/>
    <polygon points="205,120 255,150 290,145 245,110" fill="var(--lime)"/>
    <g class="body" fill="var(--text)"><text x="198" y="214">Category 1</text><text x="255" y="222">Category 2</text><text x="310" y="225">Category 3</text><text x="355" y="218">Category 4</text>
      <text x="392" y="180">Series 1</text><text x="392" y="170">Series 2</text><text x="392" y="160">Series 3</text></g>
    <g fill="var(--green)"><rect x="255" y="230" width="4" height="2"/><rect x="280" y="230" width="4" height="2"/><rect x="305" y="230" width="4" height="2"/></g>
  </svg>
</section>

<!-- Slide: 3D column chart -->
<section class="slide col-a r6">
  <svg viewBox="0 0 437 246" preserveAspectRatio="none">
    <g fill="var(--green)"><circle cx="6" cy="6" r="1.6"/><circle cx="11" cy="6" r="1.6"/><circle cx="16" cy="6" r="1.6"/></g>
    <text class="corner-mark" x="430" y="10" text-anchor="end">BLM</text>
    <circle cx="437" cy="246" r="12" fill="var(--green)"/>
    <text class="title-wide" x="218" y="28" text-anchor="middle">Chart Diagram</text>
    <rect x="200" y="34" width="20" height="2" fill="var(--green)"/><rect x="223" y="34" width="6" height="2" fill="var(--green)"/>
    <text class="body" x="218" y="44" text-anchor="middle">Lorem ipsum dolor sit amet, consectetur adipiscing elit, sed do eiusmod tempor incididunt ut labore</text>
    <text class="body" x="218" y="49" text-anchor="middle">et dolore magna aliqua ut enim ad minim veniam quis nostrud exercitation</text>
    <text class="body" x="130" y="82" text-anchor="middle" fill="var(--text)">Chart Title</text>
    <g stroke="#555" stroke-width="0.4"><path d="M30 95h190M30 115h190M30 135h190M30 155h190M30 175h190"/></g>
    <g>
      <rect x="45" y="135" width="10" height="45" fill="var(--mid)"/><rect x="58" y="125" width="10" height="55" fill="var(--green)"/><rect x="71" y="145" width="10" height="35" fill="var(--deep)"/>
      <rect x="90" y="140" width="10" height="40" fill="var(--mid)"/><rect x="103" y="115" width="10" height="65" fill="var(--green)"/><rect x="116" y="150" width="10" height="30" fill="var(--deep)"/>
      <rect x="135" y="130" width="10" height="50" fill="var(--mid)"/><rect x="148" y="140" width="10" height="40" fill="var(--green)"/><rect x="161" y="120" width="10" height="60" fill="var(--deep)"/>
      <rect x="180" y="145" width="10" height="35" fill="var(--mid)"/><rect x="193" y="95" width="10" height="85" fill="var(--lime)"/><rect x="206" y="135" width="10" height="45" fill="var(--deep)"/>
    </g>
    <g class="body" fill="var(--text)"><text x="45" y="190">Category 1</text><text x="90" y="190">Category 2</text><text x="135" y="190">Category 3</text><text x="180" y="190">Category 4</text>
      <text x="90" y="200">Series 1</text><text x="115" y="200">Series 2</text><text x="140" y="200">Series 3</text></g>
    <g>
      <circle cx="282" cy="110" r="9" fill="var(--green)"/><text class="head" x="298" y="107">consectetur adipiscing</text><text class="body" x="298" y="113">Lorem ipsum dolor sit amet sed</text><text class="body" x="298" y="118">do eiusmod tempor incididunt labore</text>
      <circle cx="282" cy="143" r="9" fill="var(--green)"/><text class="head" x="298" y="140">consectetur adipiscing</text><text class="body" x="298" y="146">Lorem ipsum dolor sit amet sed</text><text class="body" x="298" y="151">do eiusmod tempor incididunt labore</text>
      <circle cx="282" cy="176" r="9" fill="var(--green)"/><text class="head" x="298" y="173">consectetur adipiscing</text><text class="body" x="298" y="179">Lorem ipsum dolor sit amet sed</text><text class="body" x="298" y="184">do eiusmod tempor incididunt labore</text>
    </g>
  </svg>
</section>

<!-- Slide: horizontal bar chart -->
<section class="slide col-b r6">
  <svg viewBox="0 0 437 246" preserveAspectRatio="none">
    <g fill="var(--green)"><circle cx="6" cy="6" r="1.6"/><circle cx="11" cy="6" r="1.6"/><circle cx="16" cy="6" r="1.6"/></g>
    <text class="corner-mark" x="430" y="10" text-anchor="end">BLM</text>
    <circle cx="437" cy="246" r="12" fill="var(--green)"/>
    <text class="body" x="120" y="62" text-anchor="middle" fill="var(--text)">Chart Title</text>
    <g stroke="#555" stroke-width="0.4"><path d="M45 70v110M85 70v110M125 70v110M165 70v110M205 70v110"/></g>
    <g>
      <rect x="45" y="80" width="180" height="5" fill="var(--lime)"/><rect x="45" y="86" width="110" height="5" fill="var(--mid)"/><rect x="45" y="92" width="80" height="5" fill="var(--deep)"/>
      <rect x="45" y="106" width="90" height="5" fill="var(--lime)"/><rect x="45" y="112" width="150" height="5" fill="var(--mid)"/><rect x="45" y="118" width="70" height="5" fill="var(--deep)"/>
      <rect x="45" y="132" width="160" height="5" fill="var(--lime)"/><rect x="45" y="138" width="60" height="5" fill="var(--mid)"/><rect x="45" y="144" width="120" height="5" fill="var(--deep)"/>
      <rect x="45" y="158" width="100" height="5" fill="var(--lime)"/><rect x="45" y="164" width="170" height="5" fill="var(--mid)"/><rect x="45" y="170" width="90" height="5" fill="var(--deep)"/>
    </g>
    <g class="body" fill="var(--text)"><text x="18" y="90">Category 4</text><text x="18" y="116">Category 3</text><text x="18" y="142">Category 2</text><text x="18" y="168">Category 1</text>
      <text x="90" y="198">Series 1</text><text x="115" y="198">Series 2</text><text x="140" y="198">Series 3</text></g>
    <text class="title" x="250" y="77">Chart Diagram</text>
    <rect x="254" y="84" width="20" height="2" fill="var(--green)"/><rect x="277" y="84" width="6" height="2" fill="var(--green)"/>
    <g>
      <circle cx="265" cy="110" r="9" fill="var(--green)"/><text class="head" x="281" y="107">consectetur adipiscing</text><text class="body" x="281" y="113">Lorem ipsum dolor sit amet sed</text><text class="body" x="281" y="118">do eiusmod tempor incididunt labore</text>
      <circle cx="265" cy="143" r="9" fill="var(--green)"/><text class="head" x="281" y="140">consectetur adipiscing</text><text class="body" x="281" y="146">Lorem ipsum dolor sit amet sed</text><text class="body" x="281" y="151">do eiusmod tempor incididunt labore</text>
      <circle cx="265" cy="176" r="9" fill="var(--green)"/><text class="head" x="281" y="173">consectetur adipiscing</text><text class="body" x="281" y="179">Lorem ipsum dolor sit amet sed</text><text class="body" x="281" y="184">do eiusmod tempor incididunt labore</text>
    </g>
  </svg>
</section>

<!-- Slide: regional map infographic -->
<section class="slide col-a r7">
  <svg viewBox="0 0 437 246" preserveAspectRatio="none">
    <g fill="var(--green)"><circle cx="6" cy="6" r="1.6"/><circle cx="11" cy="6" r="1.6"/><circle cx="16" cy="6" r="1.6"/></g>
    <text class="corner-mark" x="430" y="10" text-anchor="end">BLM</text>
    <circle cx="437" cy="246" r="12" fill="var(--green)"/>
    <text class="title-wide" x="218" y="28" text-anchor="middle">Infographic Slide</text>
    <rect x="200" y="34" width="20" height="2" fill="var(--green)"/><rect x="223" y="34" width="6" height="2" fill="var(--green)"/>
    <text class="body" x="218" y="44" text-anchor="middle">Lorem ipsum dolor sit amet, consectetur adipiscing elit, sed do eiusmod tempor incididunt ut labore</text>
    <text class="body" x="218" y="49" text-anchor="middle">et dolore magna aliqua ut enim ad minim veniam quis nostrud exercitation</text>
    <rect x="45" y="80" width="210" height="130" rx="30" fill="var(--map)" role="img" aria-label="Regional map with two highlighted territories in green"/>
    <text class="body" x="275" y="82">Lorem ipsum dolor sit amet, consectetur</text>
    <text class="body" x="275" y="87">adipiscing elit sed do eiusmod tempor</text>
    <text class="body" x="275" y="92">incididunt ut labore et dolore magna</text>
    <text class="body" x="275" y="97">aliqua ut enim ad minim veniam</text>
    <circle cx="292" cy="125" r="14" fill="var(--white)" stroke="var(--green)" stroke-width="2"/><text x="292" y="127" text-anchor="middle" font-size="5" fill="var(--green)" font-weight="700">60%</text>
    <text class="body" x="315" y="120">Sed ut perspiciatis unde omnis</text><text class="body" x="315" y="125">iste natus error sit voluptatem</text><text class="body" x="315" y="130">accusantium doloremque laudantium totam</text>
    <circle cx="292" cy="168" r="14" fill="var(--white)" stroke="var(--green)" stroke-width="2"/><text x="292" y="170" text-anchor="middle" font-size="5" fill="var(--green)" font-weight="700">65%</text>
    <text class="body" x="315" y="163">Sed ut perspiciatis unde omnis</text><text class="body" x="315" y="168">iste natus error sit voluptatem</text><text class="body" x="315" y="173">accusantium doloremque laudantium totam</text>
  </svg>
</section>

<!-- Slide: market statistics -->
<section class="slide col-b r7">
  <svg viewBox="0 0 437 246" preserveAspectRatio="none">
    <g fill="var(--green)"><circle cx="6" cy="6" r="1.6"/><circle cx="11" cy="6" r="1.6"/><circle cx="16" cy="6" r="1.6"/></g>
    <text class="corner-mark" x="430" y="10" text-anchor="end">BLM</text>
    <circle cx="437" cy="246" r="12" fill="var(--green)"/>
    <text class="title-wide" x="218" y="28" text-anchor="middle">Market Statistics</text>
    <rect x="200" y="34" width="20" height="2" fill="var(--green)"/><rect x="223" y="34" width="6" height="2" fill="var(--green)"/>
    <text class="body" x="218" y="44" text-anchor="middle">Lorem ipsum dolor sit amet, consectetur adipiscing elit, sed do eiusmod tempor incididunt ut labore</text>
    <text class="body" x="218" y="49" text-anchor="middle">et dolore magna aliqua ut enim ad minim veniam quis nostrud exercitation</text>
    <rect x="65" y="70" width="135" height="150" rx="25" fill="var(--map)" role="img" aria-label="Country map divided into regions with several highlighted in green"/>
    <g fill="none" stroke-width="3">
      <circle cx="255" cy="112" r="19" stroke="#444"/><circle cx="255" cy="112" r="19" stroke="var(--green)" stroke-dasharray="54 120"/>
      <circle cx="318" cy="112" r="19" stroke="#444"/><circle cx="318" cy="112" r="19" stroke="var(--green)" stroke-dasharray="84 120"/>
      <circle cx="255" cy="170" r="19" stroke="#444"/><circle cx="255" cy="170" r="19" stroke="var(--green)" stroke-dasharray="113 120"/>
      <circle cx="318" cy="170" r="19" stroke="#444"/><circle cx="318" cy="170" r="19" stroke="var(--lime)" stroke-dasharray="30 120"/>
    </g>
    <g font-weight="700" font-size="9" fill="var(--green)" text-anchor="middle">
      <text x="255" y="114">45%</text><text x="318" y="114">70%</text><text x="255" y="172">95%</text><text x="318" y="172">25%</text>
    </g>
    <g class="body" text-anchor="middle"><text x="255" y="120">description</text><text x="318" y="120">description</text><text x="255" y="178">description</text><text x="318" y="178">description</text></g>
  </svg>
</section>

<!-- Slide: contact -->
<section class="slide col-a r8">
  <svg viewBox="0 0 437 246" preserveAspectRatio="none">
    <g fill="var(--green)"><circle cx="6" cy="6" r="1.6"/><circle cx="11" cy="6" r="1.6"/><circle cx="16" cy="6" r="1.6"/></g>
    <rect x="218" y="0" width="219" height="246" fill="#e9e9e6" role="img" aria-label="Street map of the venue neighbourhood"/>
    <text class="corner-mark" x="430" y="10" text-anchor="end">BLM</text>
    <text class="title" x="25" y="52">Contact Us</text>
    <rect x="29" y="59" width="20" height="2" fill="var(--green)"/><rect x="52" y="59" width="6" height="2" fill="var(--green)"/>
    <text class="label" x="25" y="72">Your Headline Here</text>
    <text class="body" x="25" y="82">Lorem ipsum is simply dummy text of the printing</text>
    <text class="body" x="25" y="87">and typesetting industry lorem ipsum has been</text>
    <text class="body" x="25" y="92">the industry standard dummy text ever since</text>
    <g>
      <circle cx="33" cy="120" r="7" fill="var(--green)"/><text class="body" x="48" y="119">Lorem ipsum dolor sit amet</text><text class="body" x="48" y="124">consectetur adipiscing elit sed</text>
      <circle cx="33" cy="155" r="7" fill="var(--green)"/><text class="body" x="48" y="154">Lorem ipsum dolor sit amet</text><text class="body" x="48" y="159">consectetur adipiscing elit sed</text>
      <circle cx="33" cy="190" r="7" fill="var(--green)"/><text class="body" x="48" y="189">Lorem ipsum dolor sit amet</text><text class="body" x="48" y="194">consectetur adipiscing elit sed</text>
    </g>
    <circle cx="205" cy="165" r="35" fill="var(--lime)"/>
    <text x="205" y="165" text-anchor="middle" fill="var(--white)" font-weight="700" font-size="10">About Us!</text>
    <text class="body" x="205" y="172" text-anchor="middle" fill="var(--white)">Lorem ipsum dolor sit</text>
  </svg>
</section>

<!-- Slide: thank you -->
<section class="slide col-b r8">
  <svg viewBox="0 0 437 246" preserveAspectRatio="none">
    <rect width="437" height="246" fill="#2e2e2e" role="img" aria-label="Dark background photo of a dining table with shared dishes"/>
    <text class="corner-mark" x="430" y="10" text-anchor="end">BLM</text>
    <rect x="0" y="60" width="437" height="82" fill="var(--green)" opacity="0.85"/>
    <circle cx="218" cy="125" r="74" fill="var(--white)"/>
    <circle cx="218" cy="125" r="70" fill="var(--lime)"/>
    <circle cx="218" cy="50" r="6" fill="var(--green)" stroke="var(--white)" stroke-width="1.5"/>
    <text x="218" y="128" text-anchor="middle" fill="var(--white)" font-weight="700" font-size="22">Thank You!</text>
    <g class="body" fill="var(--white)" text-anchor="middle">
      <text x="218" y="140">Lorem ipsum dolor sit amet consectetur</text>
      <text x="218" y="145">adipiscing elit sed do eiusmod</text>
      <text x="218" y="150">tempor incididunt ut labore et</text>
    </g>
  </svg>
</section>

</body>
</html>
```